Structural Engineering Company needs ad for magazine

We are an engineering office for structural engineering in the entertainment industry. Our focus are concert stages, festival structures, grand stands and exhibition booths. Our customers are mainly from Europe, we realize the projects worldwide. Typical customers are designer, architects, stage builders, exhibition builder and technical service provider. We are creating structural analyses, technical consulting, technical drawings and risk assessment. We are working on mid size and major events.
Some technical notes:
- CMYK profile needed, minimum 300 dpi for raster graphic
- Our primary color is Petrol. Favourite is petrol, coral and grey (black). Please use palette shown below.
- Our font in documents is Myriad. Regular at 10 pt for text and Light at 16-24pt for titles.
- The format for the ad is 61 x 127 mm (portrait) or 185 x 46 mm (landscape). Which one is up to you.
To the content:
- For contact details we just want to provide our web address "belsokar.de" and/or our e-mail "info@belsokar.de"
- Attached are some Logo files and photos.
- The ad do not advertise a specific product. It is more a general advertisement for the company.
- The language for the ad should be German. Below are keywords in English and corresponding German translation. You do not need to place all Keywords, it is just a brainstorming list to help you. You are also welcome to use other text. We will help with translation, if necessary.
- we like discussing ideas to get better results, so also if you have questions, please ask.
- If you need information that we haven't thought of yet, please ask.
Our slogan (also in Germany): event meets engineering
Service Keywords EN / DE
- Structural Analysis / Statische Berechnungen
- Risk Assessment / Risikobewertungen
- Consulting & Design / Beratung & Konstruktion
Technical Keywords EN / DE
- Stage machinery / Bühnentechnik
- Scaffolding / Gerüstbau
- Exhibition Booths / Messebauten
- Tents / Zelte
- Temporary Structures / Fliegende Bauten
- Truss / Traversen
- Stages / Bühnen
- Grand Stands / Tribünen
- Leightweight Construction / Leichtbau
- Steel Construction / Stahlbau
- Amusement Rides / Fahrgeschäfte
Look and feel
Each slider illustrates characteristics of the customer's brand and the style your logo design should communicate.

```html
<!DOCTYPE html>
<html lang="de">
<head>
<meta charset="utf-8">
<title>Belsokar – Anzeigen</title>
<link href="https://fonts.googleapis.com/css2?family=Source+Sans+3:wght@400;600;700&display=swap" rel="stylesheet">
<style>
  :root {
    --petrol: #2bb8d6;
    --ink: #0b0b0d;
    --white: #ffffff;
    --photo-dark: #2a1240;
    --photo-mid: #4b2a86;
    --photo-light: #8a3c9e;
    --stage-bg-light: #e4e4e4;
    --stage-bg-dark: #929292;
  }
  * { margin: 0; padding: 0; box-sizing: border-box; }
  html, body { width: 1200px; height: 749px; overflow: hidden; }
  body {
    position: relative;
    background: linear-gradient(115deg, var(--stage-bg-light) 0%, #b4b4b4 55%, var(--stage-bg-dark) 100%);
    font-family: "Source Sans 3", "Myriad Pro", sans-serif;
  }
  .ad { position: absolute; overflow: hidden; background: var(--petrol); }
  .ad-portrait { left: 76px; top: 60px; width: 277px; height: 575px; }
  .ad-landscape { left: 378px; top: 253px; width: 764px; height: 190px; }
  .ad-art { position: absolute; inset: 0; }
  .el { position: absolute; white-space: nowrap; }

  .brand { color: var(--white); font-weight: 600; letter-spacing: 0.22em; text-align: center; }
  .brand-portrait { left: 23px; top: 40px; width: 106px; font-size: 17px; }
  .brand-landscape { left: 648px; top: 36px; width: 102px; font-size: 16px; }

  .headline { font-weight: 600; line-height: 1; letter-spacing: -0.01em; }
  .headline .dark { color: var(--ink); }
  .headline .light { color: var(--white); }
  .headline-portrait { left: 23px; font-size: 37px; }
  .headline-landscape { left: 20px; top: 20px; font-size: 33px; }

  .pill {
    background: var(--ink); color: var(--white); font-weight: 600;
    border-radius: 12px; display: flex; align-items: center; justify-content: center;
  }
  .keywords { list-style: none; color: var(--white); }
  .keywords li { position: relative; padding-left: 17px; }
  .keywords li::before {
    content: ""; position: absolute; left: 0; top: 50%;
    width: 7px; height: 7px; margin-top: -3px;
    border: 2px solid var(--ink); border-radius: 50%;
  }

  .ad-portrait .pill { height: 22px; font-size: 15.5px; }
  .ad-portrait .keywords { font-size: 12.5px; line-height: 17.7px; left: 24px; }
  .rule-h { left: 25px; top: 405px; width: 229px; height: 1.2px; background: var(--ink); }

  .ad-landscape .pill { height: 21px; top: 65px; font-size: 14.5px; }
  .ad-landscape .keywords { font-size: 11.5px; line-height: 16.2px; top: 95px; }
  .rule-v { left: 193px; top: 98px; width: 1.2px; height: 43px; background: var(--ink); }

  .contact { display: flex; align-items: center; gap: 6px; color: var(--ink); }
  .contact svg { width: 11px; height: 11px; flex: none; }
  .ad-portrait .contact { font-size: 12.5px; }
  .ad-landscape .contact { font-size: 11.5px; top: 156px; }
</style>
</head>
<body>

<section class="ad ad-portrait" aria-label="Anzeige Hochformat">
  <svg class="ad-art" viewBox="0 0 277 575" aria-hidden="false">
    <defs>
      <linearGradient id="photoTonesP" x1="0" y1="0" x2="1" y2="1">
        <stop offset="0" stop-color="var(--photo-dark)"/>
        <stop offset="0.55" stop-color="var(--photo-mid)"/>
        <stop offset="1" stop-color="var(--photo-light)"/>
      </linearGradient>
    </defs>
    <rect width="277" height="210" fill="url(#photoTonesP)" role="img" aria-label="Foto: Bühnenscheinwerfer in violettem Licht"/>
    <path d="M0,158 L38,190 Q56,204 62,180 L66,136 Q70,110 90,128 L176,198 Q198,214 200,186 L202,142 Q206,114 230,134 L277,180 L277,575 L0,575 Z"
          fill="var(--petrol)" stroke="var(--white)" stroke-width="7" stroke-linejoin="round"/>
  </svg>

  <div class="el brand brand-portrait">BELSOKAR</div>

  <h1 class="el headline headline-portrait" style="top:220px">
    <span class="dark">Veranstaltung</span><br>
    <span class="light" style="display:inline-block;margin-top:6px">Trifft Technik</span>
  </h1>

  <div class="el pill" style="left:24px;top:309px;width:158px">Service Keywords</div>
  <ul class="el keywords" style="top:341px">
    <li>Statische Berechnungen</li>
    <li>Risikobewertungen</li>
    <li>Beratung &amp; Konstruktion</li>
  </ul>

  <div class="el rule-h"></div>

  <div class="el pill" style="left:24px;top:420px;width:170px">Technical Keywords</div>
  <ul class="el keywords" style="top:451px">
    <li>Bühnentechnik</li>
    <li>Gerüstbau</li>
    <li>Messebauten</li>
  </ul>

  <div class="el contact" style="left:23px;top:518px">
    <svg viewBox="0 0 12 12"><circle cx="6" cy="6" r="6" fill="var(--white)"/><path d="M3.6,3.2 L4.8,3 L5.3,4.4 L4.6,5 Q5.2,6.6 7,7.4 L7.6,6.7 L9,7.2 L8.8,8.4 Q5,8.6 3.6,3.2Z" fill="var(--ink)"/></svg>
    <span>+49 (0) 351 / 40 72 18 35</span>
  </div>
  <div class="el contact" style="left:23px;top:540px">
    <svg viewBox="0 0 12 12"><circle cx="6" cy="6" r="6" fill="var(--white)"/><rect x="3" y="4" width="6" height="4.4" fill="none" stroke="var(--ink)" stroke-width="0.9"/><path d="M3,4 L6,6.4 L9,4" fill="none" stroke="var(--ink)" stroke-width="0.9"/></svg>
    <span>info@belsokar.de</span>
  </div>
  <div class="el contact" style="left:160px;top:540px">
    <svg viewBox="0 0 12 12"><circle cx="6" cy="6" r="6" fill="var(--white)"/><circle cx="6" cy="6" r="3.3" fill="none" stroke="var(--ink)" stroke-width="0.8"/><ellipse cx="6" cy="6" rx="1.4" ry="3.3" fill="none" stroke="var(--ink)" stroke-width="0.8"/><path d="M2.7,6 H9.3" stroke="var(--ink)" stroke-width="0.8"/></svg>
    <span>belsokar.de</span>
  </div>
</section>

<section class="ad ad-landscape" aria-label="Anzeige Querformat">
  <svg class="ad-art" viewBox="0 0 764 190">
    <defs>
      <linearGradient id="photoTonesL" x1="0" y1="0" x2="1" y2="1">
        <stop offset="0" stop-color="var(--photo-light)"/>
        <stop offset="0.5" stop-color="var(--photo-mid)"/>
        <stop offset="1" stop-color="var(--photo-dark)"/>
      </linearGradient>
    </defs>
    <path d="M519,0 L519,12 Q520,26 532,36 L556,58 Q570,72 560,84 Q552,92 536,92 L418,95 Q394,98 392,118 Q392,132 404,146 L440,190 L764,190 L764,0 Z"
          fill="url(#photoTonesL)" stroke="var(--white)" stroke-width="7" stroke-linejoin="round"
          role="img" aria-label="Foto: Bühnenscheinwerfer in violettem Licht"/>
  </svg>

  <div class="el brand brand-landscape">BELSOKAR</div>

  <h1 class="el headline headline-landscape">
    <span class="dark">Veranstaltung</span> <span class="light">Trifft Technik</span>
  </h1>

  <div class="el pill" style="left:21px;width:145px">Service Keywords</div>
  <div class="el pill" style="left:225px;width:155px">Technical Keywords</div>

  <ul class="el keywords" style="left:21px">
    <li>Statische Berechnungen</li>
    <li>Risikobewertungen</li>
    <li>Beratung &amp; Konstruktion</li>
  </ul>
  <div class="el rule-v"></div>
  <ul class="el keywords" style="left:225px">
    <li>Bühnentechnik</li>
    <li>Gerüstbau</li>
    <li>Messebauten</li>
  </ul>

  <div class="el contact" style="left:21px">
    <svg viewBox="0 0 12 12"><circle cx="6" cy="6" r="6" fill="var(--white)"/><path d="M3.6,3.2 L4.8,3 L5.3,4.4 L4.6,5 Q5.2,6.6 7,7.4 L7.6,6.7 L9,7.2 L8.8,8.4 Q5,8.6 3.6,3.2Z" fill="var(--ink)"/></svg>
    <span>+49 (0) 351 / 40 72 18 35</span>
  </div>
  <div class="el contact" style="left:181px">
    <svg viewBox="0 0 12 12"><circle cx="6" cy="6" r="6" fill="var(--white)"/><rect x="3" y="4" width="6" height="4.4" fill="none" stroke="var(--ink)" stroke-width="0.9"/><path d="M3,4 L6,6.4 L9,4" fill="none" stroke="var(--ink)" stroke-width="0.9"/></svg>
    <span>info@belsokar.de</span>
  </div>
  <div class="el contact" style="left:314px">
    <svg viewBox="0 0 12 12"><circle cx="6" cy="6" r="6" fill="var(--white)"/><circle cx="6" cy="6" r="3.3" fill="none" stroke="var(--ink)" stroke-width="0.8"/><ellipse cx="6" cy="6" rx="1.4" ry="3.3" fill="none" stroke="var(--ink)" stroke-width="0.8"/><path d="M2.7,6 H9.3" stroke="var(--ink)" stroke-width="0.8"/></svg>
    <span>belsokar.de</span>
  </div>
</section>

</body>
</html>
```